Business Card Stationary for new Logo Skin Care Studio
BusinessCard, LetterHead, Envelope. EmailSignature, Tri-fold (background only)
Professional
Marisol Quenby
41726 Calle Ondulada #219
Mission Viejo, CA 92691
marisolquenby@postvelna.com
www.skinbymarisol.com
BusinessCard, LetterHead, Envelope. EmailSignature,
one page background (matching other stationary) that can be used for brochure
Thanks
no email address on business card!
two lines for :
next appointment;

```html
<!DOCTYPE html>
<html lang="en">
<head>
<meta charset="utf-8">
<title>Marisol's Skin Care Studio – Stationery Set</title>
<link href="https://fonts.googleapis.com/css2?family=Lato:wght@400;700&display=swap" rel="stylesheet">
<style>
:root{
  --stage:#2e2f2d;
  --paper:#ffffff;
  --green:#5aa51f;
  --green-light:#a6d23f;
  --green-dark:#1f3a12;
  --orange:#f29a1d;
  --orange-light:#f8c45a;
  --ink:#4a4a4a;
  --ink-soft:#8a8a8a;
  --shadow:rgba(0,0,0,.45);
}
*{margin:0;padding:0;box-sizing:border-box}
html,body{width:1200px;height:312px;overflow:hidden;background:var(--stage);font-family:'Lato',sans-serif}
.stage{position:relative;width:1200px;height:312px}
.piece{position:absolute;background:var(--paper);box-shadow:0 2px 6px var(--shadow);overflow:hidden}
.piece svg.bg{position:absolute;inset:0;width:100%;height:100%}
.brand{position:absolute;left:0;right:0;text-align:center;color:var(--green);font-weight:700;line-height:1}
.brand .dot{display:block;margin:0 auto 2px;border-radius:50%;background:var(--green)}
.tag{display:block;font-weight:400;color:var(--ink-soft);letter-spacing:.5px;margin-top:1px}
.tiny{position:absolute;color:var(--ink);font-size:3.6px;line-height:1.35}
.watermark{position:absolute;border-radius:50%;background:var(--green-light);opacity:.12}

/* business cards */
.card{width:84px;height:48px}
.card--front{left:24px;top:113px}
.card--back{left:115px;top:113px;background:var(--green-dark)}
.card--back .tiny{color:#e8f3d6}
.card--appt-a{left:24px;top:185px}
.card--appt-b{left:115px;top:185px}
.appt-line{position:absolute;left:8px;right:8px;height:0;border-top:.5px solid var(--ink-soft)}

/* letterheads */
.letterhead{width:230px;height:282px;top:17px}
.letterhead--a{left:228px}
.letterhead--b{left:432px}

/* envelopes */
.envelope{width:228px}
.envelope--front{left:696px;top:108px;height:108px}
.envelope--back{left:696px;top:230px;height:66px}
.envelope--flap{left:960px;width:216px}
.envelope--green{top:19px;height:96px}
.envelope--orange{top:104px;height:96px}
.envelope--white{top:190px;height:106px}
</style>
</head>
<body>
<main class="stage">

  <!-- Business card: front -->
  <section class="piece card card--front">
    <svg class="bg" viewBox="0 0 84 48" preserveAspectRatio="none">
      <path d="M0 40 Q40 30 84 38 V48 H0Z" fill="var(--green-light)"/>
      <path d="M0 43 Q40 36 84 42 V48 H0Z" fill="var(--green)"/>
    </svg>
    <div class="brand" style="top:9px;font-size:7px">
      <span class="dot" style="width:8px;height:8px"></span>Marisol's
      <span class="tag" style="font-size:3px">Skin Care Studio</span>
    </div>
  </section>

  <!-- Business card: contact side -->
  <section class="piece card card--back">
    <svg class="bg" viewBox="0 0 84 48" preserveAspectRatio="none">
      <path d="M0 0 H84 V6 Q40 12 0 4Z" fill="var(--green)"/>
    </svg>
    <div class="brand" style="top:10px;font-size:6px;color:var(--green-light)">
      <span class="dot" style="width:6px;height:6px;background:var(--green-light)"></span>Marisol's
    </div>
    <p class="tiny" style="left:6px;top:27px">Marisol Quenby · Esthetician<br>41726 Calle Ondulada #219<br>Mission Viejo, CA 92691<br>(949) 555-0182 · www.skinbymarisol.com</p>
  </section>

  <!-- Business cards: appointment side -->
  <section class="piece card card--appt-a">
    <svg class="bg" viewBox="0 0 84 48" preserveAspectRatio="none">
      <path d="M0 44 Q40 38 84 44 V48 H0Z" fill="var(--green)"/>
    </svg>
    <p class="tiny" style="left:8px;top:8px;color:var(--green);font-weight:700">Next appointment</p>
    <p class="tiny" style="left:8px;top:16px">Date</p>
    <div class="appt-line" style="top:22px"></div>
    <p class="tiny" style="left:8px;top:26px">Time</p>
    <div class="appt-line" style="top:32px"></div>
  </section>
  <section class="piece card card--appt-b">
    <svg class="bg" viewBox="0 0 84 48" preserveAspectRatio="none">
      <path d="M0 44 Q40 38 84 44 V48 H0Z" fill="var(--green)"/>
    </svg>
    <p class="tiny" style="left:8px;top:8px;color:var(--green);font-weight:700">Next appointment</p>
    <p class="tiny" style="left:8px;top:16px">Date</p>
    <div class="appt-line" style="top:22px"></div>
    <p class="tiny" style="left:8px;top:26px">Time</p>
    <div class="appt-line" style="top:32px"></div>
  </section>

  <!-- Letterhead A -->
  <section class="piece letterhead letterhead--a">
    <svg class="bg" viewBox="0 0 230 282" preserveAspectRatio="none">
      <path d="M0 250 Q110 230 230 240 V282 H0Z" fill="var(--green-light)"/>
      <path d="M0 258 Q120 242 230 252 V282 H0Z" fill="var(--green)"/>
    </svg>
    <div class="brand" style="top:18px;font-size:11px">
      <span class="dot" style="width:13px;height:13px"></span>Marisol's
      <span class="tag" style="font-size:4px">Skin Care Studio</span>
    </div>
    <div class="watermark" style="left:75px;top:110px;width:80px;height:80px"></div>
    <p class="tiny" style="left:0;right:0;top:270px;text-align:center;color:#fff">41726 Calle Ondulada #219 · Mission Viejo, CA 92691</p>
  </section>

  <!-- Letterhead B -->
  <section class="piece letterhead letterhead--b">
    <svg class="bg" viewBox="0 0 230 282" preserveAspectRatio="none">
      <path d="M0 0 H70 Q20 40 8 282 H0Z" fill="var(--green-light)"/>
      <path d="M0 0 H40 Q8 50 3 282 H0Z" fill="var(--green)"/>
      <path d="M230 200 Q170 260 120 282 H230Z" fill="var(--green-light)"/>
      <path d="M230 225 Q190 265 160 282 H230Z" fill="var(--green)"/>
    </svg>
    <div class="brand" style="top:18px;font-size:11px">
      <span class="dot" style="width:13px;height:13px"></span>Marisol's
      <span class="tag" style="font-size:4px">Skin Care Studio</span>
    </div>
    <div class="watermark" style="left:75px;top:110px;width:80px;height:80px"></div>
    <p class="tiny" style="left:20px;top:270px">www.skinbymarisol.com</p>
  </section>

  <!-- Envelope front -->
  <section class="piece envelope envelope--front">
    <svg class="bg" viewBox="0 0 228 108" preserveAspectRatio="none">
      <path d="M0 0 H228 V10 Q110 22 0 8Z" fill="var(--green)"/>
      <path d="M0 98 Q110 90 228 100 V108 H0Z" fill="var(--green-light)"/>
    </svg>
    <div class="brand" style="top:20px;left:10px;right:auto;width:60px;font-size:7px">
      <span class="dot" style="width:8px;height:8px"></span>Marisol's
    </div>
    <p class="tiny" style="left:12px;top:42px">41726 Calle Ondulada #219<br>Mission Viejo, CA 92691</p>
  </section>

  <!-- Envelope back -->
  <section class="piece envelope envelope--back">
    <svg class="bg" viewBox="0 0 228 66" preserveAspectRatio="none">
      <path d="M0 0 L114 30 L228 0" fill="none" stroke="#e2e2e2" stroke-width="1"/>
      <path d="M0 60 Q110 54 228 60 V66 H0Z" fill="var(--green)"/>
    </svg>
    <p class="tiny" style="left:0;right:0;top:50px;text-align:center">www.skinbymarisol.com</p>
  </section>

  <!-- Flap envelopes -->
  <section class="piece envelope envelope--flap envelope--green">
    <svg class="bg" viewBox="0 0 216 96" preserveAspectRatio="none">
      <path d="M0 0 H216 V30 Q108 80 0 30Z" fill="var(--green)"/>
      <path d="M0 0 H216 V22 Q108 66 0 22Z" fill="var(--green-light)"/>
    </svg>
    <div class="brand" style="top:10px;font-size:6px;color:#fff">
      <span class="dot" style="width:7px;height:7px;background:#fff"></span>Marisol's
    </div>
  </section>
  <section class="piece envelope envelope--flap envelope--orange">
    <svg class="bg" viewBox="0 0 216 96" preserveAspectRatio="none">
      <path d="M0 0 H216 V30 Q108 80 0 30Z" fill="var(--orange)"/>
      <path d="M0 0 H216 V22 Q108 66 0 22Z" fill="var(--orange-light)"/>
    </svg>
    <div class="brand" style="top:10px;font-size:6px;color:#fff">
      <span class="dot" style="width:7px;height:7px;background:#fff"></span>Marisol's
    </div>
  </section>
  <section class="piece envelope envelope--flap envelope--white">
    <svg class="bg" viewBox="0 0 216 106" preserveAspectRatio="none">
      <path d="M0 0 L108 44 L216 0" fill="none" stroke="#dcdcdc" stroke-width="1"/>
    </svg>
    <div class="brand" style="top:14px;font-size:6px">
      <span class="dot" style="width:7px;height:7px"></span>Marisol's
    </div>
  </section>

</main>
</body>
</html>
```